Mane Glow...restoring shine to tired, brittle locks!

We are launching a luxurious, all-natural line of handmade hair products. These products will compete against a host of other not-so natural products targeting women with coily, kinky curly hair and the desire to grow (or re-grow) their tresses. Our product is different and we want our brand to reflect that. Mane Glow is about bringing 'life back' to dry, damaged hair. Our product will be bottled in black or blue bottles and we'd love to see lime green accents in the concepts.

Target Market(s)

21 - 50 year old women with wavy, coily, curly or kinky hair.

Industry/Entity Type

Hair Care Product

Colors
add136
ffffff

Requirements
Must have
• Label must be "ready for retail" and catch a consumers eye when competing against other products. Should also look great online.
Nice to have
• Would love the label to include a symbol of "Life" or growth. The base of all the products is a plant called Moringa which is plant/superfood used in Africa and India. More information about Moringa can be found here
• http://www.plumtorvex.com/articles/amazing-benefits-of-moringa-plant/
• Some of the benefits of Moringa include:
• Builds collagen fibers and minimize the appearance of fine wrinkle lines (Vitamin A)
• - Minimizes the appearance of fine wrinkle lines. (Vitamin C)
• - Improves moisturizing, softness and smoothness. (Vitamin E)
• - Delays the aging process
• - Helps build collagen which improves skin conditions
• - Is a natural healing emollient
• - Helps with dry, rough skin conditions like eczema, psoriasis and dermatitis.
• - Protects your skin from environmental damage
• - Helps improve scalp circulation (which aids in preventing hair loss)
• - Helps improve split ends in hair

```html
<!DOCTYPE html>
<html lang="en">
<head>
<meta charset="utf-8">
<title>Mane Glow – Label Set</title>
<link href="https://fonts.googleapis.com/css2?family=Montserrat:wght@400;600;700&family=Questrial&display=swap" rel="stylesheet">
<style>
:root{
  --lime:#add136;
  --lime-deep:#8cab22;
  --ink:#1d1d1b;
  --paper:#ffffff;
  --nut-dark:#6b3a1c;
  --nut-light:#b98a5e;
  --leaf:#6fae3a;
}
*{margin:0;padding:0;box-sizing:border-box}
html,body{width:1200px;height:638px;overflow:hidden;background:var(--paper)}
body{position:relative;font-family:"Montserrat",Arial,sans-serif;color:var(--ink)}
.label{position:absolute;background:var(--paper);border:1.5px solid var(--ink);overflow:hidden}
.brand{display:flex;align-items:center;justify-content:center;gap:6px;font-family:"Questrial",Arial,sans-serif;color:var(--lime-deep);white-space:nowrap}
.brand-dot{border-radius:50%;background:var(--ink);flex:none}
.tagline-bar{background:var(--lime);color:var(--paper);font-family:"Questrial",Arial,sans-serif;text-align:center;white-space:nowrap}
.title{color:var(--lime-deep);font-weight:700;text-align:center}
.sub{text-align:center}
.photo{position:absolute}
.nuts{background:radial-gradient(ellipse at 45% 50%,var(--nut-light) 0%,var(--nut-dark) 42%,#eef2e0 66%,rgba(255,255,255,0) 74%)}
.aloe{background:radial-gradient(ellipse at 45% 55%,var(--leaf) 0%,#9ccc6a 42%,#eef3e3 66%,rgba(255,255,255,0) 74%)}
.footer-band{position:absolute;left:0;right:0;bottom:0;background:var(--lime);color:var(--paper);text-align:center}
.seal{position:absolute;border-radius:50%;background:var(--lime);border:3px solid var(--paper);box-shadow:0 0 0 1px #d6e6a0;color:var(--paper);font-weight:700;display:flex;align-items:center;justify-content:center;text-align:center}

/* round tin label */
.tin{left:108px;top:190px;width:236px;height:236px;border-radius:50%}
.tin .brand{position:absolute;top:12px;left:0;right:0;font-size:19px}
.tin .brand-dot{width:7px;height:7px}
.tin .tagline-bar{position:absolute;top:46px;left:0;right:0;height:10px;font-size:7px;line-height:10px}
.tin .title{position:absolute;top:62px;left:0;right:0;font-size:8px}
.tin .sub{position:absolute;top:73px;left:0;right:0;font-size:7px;line-height:9px}
.tin .photo{left:45px;top:94px;width:130px;height:100px}
.tin .footer-band{height:28px;font-size:6px;padding-top:6px}

/* soap bar label */
.bar{left:347px;top:210px;width:166px;height:214px;border-radius:8px}
.bar .brand{position:absolute;top:10px;left:0;right:0;font-size:21px}
.bar .brand-dot{width:7px;height:7px}
.bar .tagline-bar{position:absolute;top:46px;left:0;right:0;height:9px;font-size:6.5px;line-height:9px}
.bar .title{position:absolute;top:60px;left:0;right:0;font-size:11px}
.bar .sub{position:absolute;top:73px;left:0;right:0;font-size:6.5px;line-height:9px}
.bar .photo{left:28px;top:92px;width:120px;height:90px}
.bar .footer-band{height:36px;font-size:4.6px;line-height:6.2px;padding:4px 6px}

/* bottle labels */
.bottle{top:25px;width:243px;height:400px;border-radius:8px}
.front{left:555px}
.back{left:808px}
.bottle .brand{position:absolute;top:30px;left:0;right:0;font-size:36px}
.bottle .brand-dot{width:12px;height:12px}
.bottle .tagline-bar{position:absolute;top:80px;left:0;right:0;height:20px;font-size:11px;line-height:20px}
.front .title{position:absolute;top:110px;left:0;right:0;font-size:17px}
.front .sub{position:absolute;top:131px;left:0;right:0;font-size:12px}
.front .photo{left:25px;top:148px;width:185px;height:180px}
.front .seal{left:150px;top:244px;width:82px;height:82px;font-size:6.5px;line-height:8.5px;padding:8px}
.bottle .footer-band{height:76px;font-size:9px;line-height:11px;padding-top:9px}
.bottle .footer-band .size{font-size:11px;font-weight:700;margin-top:6px}
.back .body{position:absolute;left:18px;right:18px;top:118px;font-size:10px;line-height:12px}
.back .body h3{font-size:10px;font-weight:700;margin:0 0 10px}
.back .body p{margin-bottom:12px}

/* wrap label */
.wrap{left:24px;top:449px;width:1152px;height:164px;background:var(--lime)}
.wrap .info{position:absolute;left:64px;top:12px;width:360px;color:var(--paper);font-size:10px;line-height:12px}
.wrap .info .claims{font-weight:700;margin-bottom:10px}
.wrap .info h3{font-size:10.5px;font-weight:700;margin:0 0 9px}
.wrap .info p{margin-bottom:12px}
.wrap .info .ingredients{font-size:9.5px;line-height:11.5px}
.wrap .face{position:absolute;left:437px;top:0;width:647px;height:163px;background:var(--paper)}
.wrap .face .brand{position:absolute;left:44px;top:20px;font-size:34px;justify-content:flex-start}
.wrap .face .brand-dot{width:11px;height:11px}
.wrap .face .size{position:absolute;left:283px;top:30px;font-size:12px;font-weight:700}
.wrap .face .tagline-bar{position:absolute;left:0;top:82px;width:358px;height:18px;font-size:12px;line-height:18px;text-align:left;padding-left:40px}
.wrap .face .title{position:absolute;left:36px;top:107px;font-size:14px;text-align:left}
.wrap .face .sub{position:absolute;left:36px;top:125px;width:320px;font-size:12px;line-height:14px;text-align:left}
.wrap .face .photo{left:370px;top:8px;width:130px;height:148px}
.wrap .face .seal{left:498px;top:68px;width:84px;height:84px;font-size:6.5px;line-height:8.5px;padding:8px}
.wrap .spine{position:absolute;right:0;top:0;width:68px;height:164px;color:var(--paper);font-size:8px;line-height:11px}
.wrap .spine span{position:absolute;left:50%;top:50%;transform:translate(-50%,-50%) rotate(-90deg);white-space:nowrap;text-align:center}
</style>
</head>
<body>

<section class="label tin" aria-label="Leave-in conditioner lid label">
  <div class="brand"><span class="brand-dot"></span>Mane Glow</div>
  <div class="tagline-bar">Restore shine to tired, brittle locks</div>
  <div class="title">THE RENEWER LEAVE-IN CONDITIONER</div>
  <div class="sub">Intense moisture, repair and growth treatment<br>With Moringa and Shea</div>
  <div class="photo nuts" role="img" aria-label="Shea nuts with white moringa blossoms"></div>
  <div class="footer-band">www.maneglowgoods.com</div>
</section>

<section class="label bar" aria-label="Shampoo bar label">
  <div class="brand"><span class="brand-dot"></span>Mane Glow</div>
  <div class="tagline-bar">Restore shine to tired, brittle locks</div>
  <div class="title">TWO-IN-ONE</div>
  <div class="sub">Moisturizing &amp; Conditioning Shampoo Bar<br>With Moringa and Aloe Leaf</div>
  <div class="photo aloe" role="img" aria-label="Aloe leaves with white moringa blossoms"></div>
  <div class="footer-band">How to Use:<br>Great for travel. Wet hair and rub the bar from root to tip to lather. Rinse and repeat. Let the bar dry after use.<br>MADE IN THE USA | www.maneglowgoods.com</div>
</section>

<section class="label bottle front" aria-label="The Revival oil front label">
  <div class="brand"><span class="brand-dot"></span>Mane Glow</div>
  <div class="tagline-bar">Restore shine to tired, brittle locks</div>
  <div class="title">THE REVIVAL</div>
  <div class="sub">Moringa and Castor Oil</div>
  <div class="photo nuts" role="img" aria-label="Castor beans with white moringa blossoms"></div>
  <div class="seal">No sulfites, mineral oils or synthetic ingredients in this precious oil</div>
  <div class="footer-band">
    Daily, nourishing hair and scalp oil<br>All Natural - Hand-Made<br>Paraben-free<br>For daily sealing and care of all hair textures
    <div class="size">4 oz (118 ml)</div>
  </div>
</section>

<section class="label bottle back" aria-label="The Revival oil back label">
  <div class="brand"><span class="brand-dot"></span>Mane Glow</div>
  <div class="tagline-bar">Restore shine to tired, brittle locks</div>
  <div class="body">
    <h3>How to Use:</h3>
    <p>Massage into scalp daily to stimulate growth. Use as a hot oil treatment. Apply from root to tip and to seal ends.</p>
    <h3>The Revival All Natural Ingredients:</h3>
    <p>Moringa Oil, African Castor Oil, Grapeseed Oil, Avocado Oil, Sunflower Oil, Pumpkin Seed Oil, Pumpkin Seed Extract, Green Tea Extract, Nettle Extract, Essential of Rosemary, Lemon, Green Tea, Patchouli, Cedarwood, Sage, Chamomile and Lavender</p>
  </div>
  <div class="footer-band">
    MADE IN THE USA<br>www.maneglowgoods.com
    <div class="size" style="margin-top:18px">4 oz (118 ml)</div>
  </div>
</section>

<section class="label wrap" aria-label="Leave-in conditioner wrap label">
  <div class="info">
    <div class="claims">ALL NATURAL • HAND-MADE • PARABEN-FREE</div>
    <h3>How to Use:</h3>
    <p>Can be used on wet or dry hair. Part hair gently and apply from root to tips. Watch tresses come back to life instantly.</p>
    <h3>Moringa Restore All Natural Ingredients:</h3>
    <p class="ingredients">Moringa Oil, Shea Butter, Grape Seed Oil infused with Chickweed, Chamomile Flowers, Cleavers, Nettle Leaves, Rosemary, Tea Tree, Cedarwood, Lavendar, Chamomile and Vitamin E.</p>
  </div>
  <div class="face">
    <div class="brand"><span class="brand-dot"></span>Mane Glow</div>
    <div class="size">4 oz (118 ml)</div>
    <div class="tagline-bar">Restore shine to tired, brittle locks</div>
    <div class="title">THE RENEWER LEAVE-IN CONDITIONER</div>
    <div class="sub">Intense moisture, repair and growth treatment that transforms troubled tresses in minutes</div>
    <div class="photo nuts" role="img" aria-label="Shea nuts with white moringa blossoms"></div>
    <div class="seal">No sulfites, mineral oils or synthetic ingredients in this precious oil</div>
  </div>
  <div class="spine"><span>MADE IN THE USA<br>www.maneglowgoods.com</span></div>
</section>

</body>
</html>
```